Real Estate - Car Wrap - Graphic design work for bus advertisement

Looking for graphic design work for Martin Fairwell - Real Estate Associate. Name of the company is Fairwell Property Services. Slogan is:
Homes Found Keys Turned - We would really like to see the slogan used.

In need of an ad design that will be used for a bus ad. Bus ad specs included in attachments.

Bus ad info (Must include)
Martin Fairwell
Homeline Prime logo
Martin's phone number is 780-555-0143
Website is: Fairwellproperty.example
I have included the bus ad dimensions in the attachments

Our color scheme is Black & White with a hint of Navy Blue and we are open to a little bit of gold to add a little bit of color. We like the idea of the ad being in black and white and then just adding a hint of blue. Martins photo might be nice black and white. Open to ideas on this.

The final design should communicate professionalism, strength and approachability while being eye catching with a bit of wow factor. Something clean and modern with potentially some interesting graphic work.

Our ad design must incorporate the Homeline Prime Logo doesn't have to be in the color red like attached photo. It can be in any color that goes well with the ad just needs to be present.

We love the attached ad idea that I have included to help give some idea of where we are going. No purple however we want to stick with the Navy as the main color choice.

The dimensions for the bus ad are are attached in specs for the bus.
We really like the idea of using the head shot of Martin standing in the blue shirt for the bus ad, (can be in color or black and white) We are however open to the other photo in attachments. Looking to see what you come up with.

I have included Martin's name written in more of a signature font like the ad idea has. We want something in more of a signature for his name. See Signature for Martin Fairwell for ex. Something as close to this as possible. Needs to be very easy to read from afar. Please don't include the strength of housing that is on this photo. We don't like this slogan.

I have attached, head shots of Martin, Our companies current logo which is the house and an overall picture idea of the look we are going for. We really like this ad for an idea, black and white with a splash of color at the bottom. Again our color is Navy Blue.

Please message me if you have questions.
Thank you,

Lena Fairwell

Please note that Martin’s photo needs to be on the business card. We also do not want any purple color in the design. The ad example image is just to give an idea of something we like. Thank you

Industry/Entity Type

Real Estate Agent

Font styles to use
Script

Requirements
Must have
• Colors are black and white with accent navy
Nice to have
• Open to a hint of gold
Should not have
• Any purple or light blue colors

```html
<!DOCTYPE html>
<html lang="en">
<head>
<meta charset="utf-8">
<title>Fairwell Property Services – Bus Ad</title>
<link href="https://fonts.googleapis.com/css2?family=Montserrat:wght@300;500;800;900&family=Great+Vibes&display=swap" rel="stylesheet">
<style>
  :root {
    --paper: #ffffff;
    --charcoal: #151515;
    --charcoal-soft: #232323;
    --navy: #13224a;
    --gold: #f5c20f;
    --white: #ffffff;
    --photo-top: #3a3d55;
    --photo-bottom: #14183a;
  }
  * { margin: 0; padding: 0; box-sizing: border-box; }
  html, body { width: 1200px; height: 305px; overflow: hidden; background: var(--paper); }
  .ad {
    position: relative; width: 1200px; height: 305px;
    font-family: "Montserrat", sans-serif; color: var(--white);
  }
  .ad-band {
    position: absolute; left: 8px; top: 25px; width: 1190px; height: 257px;
    background: radial-gradient(ellipse at 40% 40%, var(--charcoal-soft), var(--charcoal) 70%);
  }
  .ad-frame {
    position: absolute; left: 40px; top: 46px; width: 1126px; height: 215px;
    border: 4px solid var(--white);
  }
  .agent-photo {
    position: absolute; left: 75px; top: 37px; width: 172px; height: 245px;
    background: linear-gradient(180deg, var(--photo-top), var(--photo-bottom));
    border-radius: 60px 60px 0 0;
  }
  .agent-signature {
    position: absolute; left: 270px; top: 172px; width: 180px;
  }
  .agent-signature .name {
    font-family: "Great Vibes", cursive; font-size: 38px; line-height: 1;
    color: var(--white); white-space: nowrap;
  }
  .agent-signature .title {
    margin-top: 6px; text-align: right;
    font-size: 5.6px; font-weight: 500; letter-spacing: 1.6px; color: var(--gold);
  }
  .brand-block {
    position: absolute; left: 557px; top: 76px; width: 233px;
  }
  .brand-block .line {
    display: block; text-align: justify; text-align-last: justify;
    line-height: 1; white-space: nowrap;
  }
  .brand-name { font-size: 26px; font-weight: 300; height: 34px; }
  .brand-word { font-size: 25px; font-weight: 900; height: 34px; }
  .slogan { margin-top: 12px; color: var(--gold); }
  .slogan .line { font-size: 18px; font-weight: 500; height: 23px; }
  .contact-panel {
    position: absolute; left: 833px; top: 25px; width: 265px; height: 256px;
    background: var(--navy);
  }
  .brokerage {
    position: absolute; left: 13px; top: 40px;
    display: flex; align-items: center; gap: 6px;
    font-size: 12px; font-weight: 800; letter-spacing: .3px;
  }
  .brokerage .dot { width: 9px; height: 9px; border-radius: 50%; background: var(--white); }
  .phone {
    position: absolute; left: 13px; top: 92px; width: 240px;
    font-size: 32px; font-weight: 900; letter-spacing: -.3px; white-space: nowrap;
  }
  .website {
    position: absolute; left: 13px; top: 169px; width: 239px; height: 37px;
    background: var(--gold); color: var(--navy);
    display: flex; align-items: center; justify-content: center;
    font-size: 12.5px; font-weight: 500; letter-spacing: .2px;
  }
</style>
</head>
<body>
  <div class="ad">
    <div class="ad-band"></div>
    <div class="ad-frame"></div>

    <div class="agent-photo" role="img" aria-label="Portrait of Martin Fairwell in a navy suit"></div>

    <div class="agent-signature">
      <div class="name">Martin Fairwell</div>
      <div class="title">REAL ESTATE AGENT</div>
    </div>

    <div class="brand-block">
      <span class="line brand-name">FAIRWELL</span>
      <span class="line brand-word">PROPERTY</span>
      <span class="line brand-word">SERVICES</span>
      <div class="slogan">
        <span class="line">HOMES FOUND</span>
        <span class="line">KEYS TURNED</span>
      </div>
    </div>

    <div class="contact-panel">
      <div class="brokerage"><span>HOMELINE PRIME</span><span class="dot"></span></div>
      <div class="phone">780-555-0143</div>
      <div class="website">FAIRWELLPROPERTY.EXAMPLE</div>
    </div>
  </div>
</body>
</html>
```